Business Cards for Tech Company - Norvale

We would like new modern business cards designed for our company. Attached are some examples of other business cards we like. <br/><br/>Info we need is: <br/>First Name, Last Name<br/>Address<br/>Store Phone<br/>Cell Phone<br/>Email Address<br/>Text Logo <br/>And Other Logo<br/>

Industry/Entity Type

Technology Equipment

Contact Information for Business Card

Please use these details as example:

Dale Morrow
Technology Specialist
Direct 555.617.2094
Phone 555-730-8186

dale.morrow@norvale.example

2971 Willet Lane
Carrow Falls, NE 00427

Font styles to use
Sans Serif
Other font styles liked:
• Anything easy to read and modern

Colors

Designer to choose colors to be used in the design.

Requirements
Must have
• Both Logos
• Signature as name
• Use the text logo and use the shark logo but do not use the full shark logo. Have it where it is zoomed in and is expanding out of the card.
Nice to have
• Keep it clean and modern
• We like blue, white, and black/grays.
Should not have
• Random icons for phone and address.

```html
<!DOCTYPE html>
<html lang="en">
<head>
<meta charset="utf-8">
<title>Norvale Business Cards</title>
<link rel="stylesheet" href="https://fonts.googleapis.com/css2?family=Allura&family=Montserrat:wght@400;800&display=swap">
<style>
  :root {
    --stage: #1f1f1f;
    --card-gray: #6e6e6e;
    --logo-gray: #6b6b6b;
    --white: #ffffff;
    --blue: #4470c0;
    --teal: #7ecfcf;
  }
  * { margin: 0; padding: 0; box-sizing: border-box; }
  html, body {
    width: 1200px; height: 900px; overflow: hidden;
    background: var(--stage);
    font-family: "Montserrat", sans-serif;
  }
  .stage {
    width: 1200px; height: 900px;
    display: flex; flex-direction: column;
    align-items: center; justify-content: center; gap: 40px;
  }
  .card {
    position: relative; width: 700px; height: 400px;
    overflow: hidden;
  }
  .card-back { background: var(--card-gray); }
  .card-front { background: var(--white); }

  .wordmark {
    position: absolute;
    font-family: "Montserrat", sans-serif;
    font-weight: 800;
    font-size: 62px;
    letter-spacing: -1px;
    line-height: 1;
  }
  .card-back .wordmark { left: 90px; top: 120px; color: var(--white); }
  .card-front .wordmark { left: 190px; top: 50px; color: var(--logo-gray); }

  .mascot-area {
    position: absolute; right: -60px; top: 60px;
    width: 260px; height: 380px;
    border-radius: 50% 0 0 50%;
    background: linear-gradient(160deg, var(--blue) 35%, var(--teal) 100%);
  }

  .wave { position: absolute; inset: 0; }

  .identity {
    position: absolute; left: 42px; top: 198px; color: var(--white);
  }
  .signature {
    font-family: "Allura", cursive;
    font-size: 54px; line-height: 1; margin-bottom: 4px;
  }
  .role, .address {
    font-size: 19px; font-weight: 400; line-height: 1.3;
  }
  .role { margin-bottom: 10px; }

  .contacts {
    position: absolute; right: 30px; bottom: 26px;
    list-style: none; color: var(--white);
    font-size: 19px; line-height: 1.55; text-align: right;
  }
  .contacts li { display: flex; align-items: center; justify-content: flex-end; gap: 10px; }
  .contacts svg { width: 20px; height: 20px; flex: none; }
</style>
</head>
<body>
<main class="stage">

  <section class="card card-back">
    <div class="wordmark">Norvale</div>
    <div class="mascot-area" role="img" aria-label="Zoomed-in brand mascot emerging from the card edge"></div>
  </section>

  <section class="card card-front">
    <svg class="wave" viewBox="0 0 700 400" aria-hidden="true">
      <defs>
        <linearGradient id="waveFill" x1="0" y1="0" x2="1" y2="1">
          <stop offset="0.35" stop-color="#4470c0"/>
          <stop offset="1" stop-color="#7ecfcf"/>
        </linearGradient>
      </defs>
      <path d="M0,152 C220,110 470,140 700,290 L700,400 L0,400 Z" fill="var(--blue)"/>
      <path d="M0,160 C220,120 470,148 700,292 L700,400 L0,400 Z" fill="var(--card-gray)"/>
      <path d="M0,192 C220,142 480,172 700,294 L700,400 L0,400 Z" fill="url(#waveFill)"/>
    </svg>

    <div class="wordmark">Norvale</div>

    <div class="identity">
      <div class="signature">Dale Morrow</div>
      <div class="role">Technology Specialist</div>
      <div class="address">2971 Willet Lane<br>Carrow Falls, NE 00427</div>
    </div>

    <ul class="contacts">
      <li>555.617.2094
        <svg viewBox="0 0 24 24" fill="none" stroke="#fff" stroke-width="1.8"><path d="M5 3h4l2 5-2.5 1.5a11 11 0 0 0 6 6L16 13l5 2v4a2 2 0 0 1-2 2A17 17 0 0 1 3 5a2 2 0 0 1 2-2z"/></svg>
      </li>
      <li>555-730-8186
        <svg viewBox="0 0 24 24" fill="none" stroke="#fff" stroke-width="1.8"><rect x="7" y="2" width="10" height="20" rx="2"/><line x1="11" y1="18" x2="13" y2="18"/></svg>
      </li>
      <li>dale.morrow@norvale.example
        <svg viewBox="0 0 24 24" fill="none" stroke="#fff" stroke-width="1.8"><rect x="2" y="5" width="20" height="14"/><path d="M2 5l10 8 10-8"/></svg>
      </li>
    </ul>
  </section>

</main>
</body>
</html>
```